Electronics Projects Site Flyer (you know, microcontrollers, resistors, LEDs, GEEKY stuff)

We host two sites, one retail and another is an informational type.

We need a flyer that will entice customers from the retail site to visit our informational website. The informational site is a place where people can share neat home made and semi-professional electronics projects alike. More importantly it's about talking shop about electronics.

There is a strong culture of talking about what's new in the DIY electronics scene. Some popular topics are Zorvex Microcontrollers, Brimelo, Test Equipment, Software, products like the ZorKit 2, Quandry Logic Analyser and so on. GEEKY stuff :)

I would like to see our site logo used www.volt-tinker(dot)com and for the flyer to communicate "Visit Volt Tinker today"

Flyer size: A5
I would also like to have a A6 variant produced, if possible.
Updates

Target Market(s)

18-25 yr/old males, people interested with electronics and microcontrollers

Industry/Entity Type

Electronics

Requirements
Must have
• Our logo (attached)

Be creatively enticing

A5 flyer size
Nice to have
• Ability to have A6 flyer variant

```html
<!DOCTYPE html>
<html lang="en">
<head>
<meta charset="utf-8">
<title>Volt Tinker Flyer – A5 and A6</title>
<link rel="stylesheet" href="https://fonts.googleapis.com/css2?family=Roboto+Condensed:wght@700&family=Arimo:wght@400&display=swap">
<style>
  :root {
    --navy: #12275a;
    --silver-dark: #8f9399;
    --silver-light: #f4f4f4;
    --sky-pale: #e9f4fa;
    --sky: #7cc2e2;
    --sky-deep: #3a98cc;
    --teal-light: #8fd3e3;
    --teal: #1aa0c0;
    --teal-deep: #0b7fa3;
    --white: #ffffff;
    --label: #333333;
    --frame: #444444;
    --slate-top: #3b5186;
    --slate-mid: #3a3f48;
    --slate-low: #8a8f96;
  }
  html, body {
    margin: 0;
    padding: 0;
    width: 900px;
    height: 1200px;
    overflow: hidden;
    background: var(--white);
  }
  .sheet {
    position: relative;
    width: 900px;
    height: 1200px;
  }
  .size-label {
    position: absolute;
    font-family: "Arimo", Arial, sans-serif;
    font-size: 26px;
    color: var(--label);
    margin: 0;
  }
  .size-label--a5 { left: 27px; top: 393px; }
  .size-label--a6 { left: 144px; top: 893px; }

  .flyer {
    position: absolute;
    width: 795px;
    height: 561px;
    overflow: hidden;
    box-sizing: border-box;
    outline: 2px solid var(--frame);
    outline-offset: -1px;
    background: linear-gradient(100deg, var(--sky-pale) 0%, var(--sky) 30%, var(--sky-deep) 70%);
    font-family: "Roboto Condensed", "Arial Narrow", sans-serif;
  }
  .flyer--a5 { left: 78px; top: 105px; }
  .flyer--a6 {
    left: 194px;
    top: 697px;
    transform: scale(0.708);
    transform-origin: top left;
    outline-width: 3px;
  }

  .flyer__band-top {
    position: absolute;
    left: 0; top: 0;
    width: 100%; height: 43px;
    background: var(--navy);
  }
  .flyer__stripe {
    position: absolute;
    left: 0; top: 43px;
    width: 100%; height: 24px;
    background: linear-gradient(90deg, var(--silver-dark) 0%, #d7d8da 35%, var(--silver-light) 75%, var(--white) 100%);
  }
  .flyer__band-lower {
    position: absolute;
    left: 0; top: 67px;
    width: 100%; height: 90px;
    background: var(--navy);
  }

  .flyer__site-view {
    position: absolute;
    left: 0; top: 0;
    width: 795px; height: 561px;
  }

  .flyer__badge {
    position: absolute;
    left: 32px; top: 25px;
    width: 280px; height: 280px;
    border-radius: 50%;
    background: var(--white);
    box-shadow: 0 3px 10px rgba(0, 0, 0, 0.25);
  }
  .flyer__badge-disc {
    position: absolute;
    left: 14px; top: 14px;
    width: 252px; height: 252px;
    border-radius: 50%;
    background: linear-gradient(160deg, var(--teal-light) 0%, var(--teal) 55%, var(--teal-deep) 100%);
  }
  .flyer__headline {
    position: absolute;
    left: 52px; top: 56px;
    margin: 0;
    color: var(--white);
    font-size: 42px;
    line-height: 54px;
    letter-spacing: 0.2px;
    text-shadow: 1px 2px 3px rgba(0, 0, 0, 0.35);
  }

  .flyer__brand {
    position: absolute;
    left: 420px; top: 100px;
    display: flex;
    align-items: center;
    gap: 14px;
    margin: 0;
    color: var(--white);
    font-size: 60px;
    line-height: 1;
  }
  .flyer__brand-mark {
    width: 22px; height: 22px;
    background: var(--white);
  }

  .flyer__url-band {
    position: absolute;
    left: 0; top: 437px;
    width: 100%; height: 68px;
    background: rgba(255, 255, 255, 0.28);
  }
  .flyer__url {
    position: absolute;
    left: 22px; top: 438px;
    margin: 0;
    color: var(--white);
    font-size: 64px;
    line-height: 68px;
    text-shadow: 1px 2px 3px rgba(0, 0, 0, 0.4);
  }
</style>
</head>
<body>
<main class="sheet">
  <p class="size-label size-label--a5">A5</p>
  <article class="flyer flyer--a5" aria-label="A5 flyer">
    <div class="flyer__band-top"></div>
    <div class="flyer__stripe"></div>
    <div class="flyer__band-lower"></div>
    <svg class="flyer__site-view" viewBox="0 0 795 561" role="img" aria-label="Tilted screenshot of the Volt Tinker website with project photos and an article">
      <defs>
        <linearGradient id="siteA5" x1="0" y1="0" x2="0" y2="1">
          <stop offset="0" stop-color="var(--slate-top)"/>
          <stop offset="0.3" stop-color="var(--slate-mid)"/>
          <stop offset="1" stop-color="var(--slate-low)"/>
        </linearGradient>
      </defs>
      <polygon points="245,272 795,172 795,561 415,561" fill="url(#siteA5)"/>
    </svg>
    <div class="flyer__badge">
      <div class="flyer__badge-disc"></div>
      <h1 class="flyer__headline">Visit<br>Volt Tinker<br>today</h1>
    </div>
    <p class="flyer__brand"><span>Volt Tinker</span><span class="flyer__brand-mark"></span></p>
    <div class="flyer__url-band"></div>
    <p class="flyer__url">volt-tinker.com</p>
  </article>

  <p class="size-label size-label--a6">A6</p>
  <article class="flyer flyer--a6" aria-label="A6 flyer">
    <div class="flyer__band-top"></div>
    <div class="flyer__stripe"></div>
    <div class="flyer__band-lower"></div>
    <svg class="flyer__site-view" viewBox="0 0 795 561" role="img" aria-label="Tilted screenshot of the Volt Tinker website with project photos and an article">
      <defs>
        <linearGradient id="siteA6" x1="0" y1="0" x2="0" y2="1">
          <stop offset="0" stop-color="var(--slate-top)"/>
          <stop offset="0.3" stop-color="var(--slate-mid)"/>
          <stop offset="1" stop-color="var(--slate-low)"/>
        </linearGradient>
      </defs>
      <polygon points="245,272 795,172 795,561 415,561" fill="url(#siteA6)"/>
    </svg>
    <div class="flyer__badge">
      <div class="flyer__badge-disc"></div>
      <h2 class="flyer__headline">Visit<br>Volt Tinker<br>today</h2>
    </div>
    <p class="flyer__brand"><span>Volt Tinker</span><span class="flyer__brand-mark"></span></p>
    <div class="flyer__url-band"></div>
    <p class="flyer__url">volt-tinker.com</p>
  </article>
</main>
</body>
</html>
```